We are having a Fresh Start, Bold Body Makeover Contest at our fitness studio. We need a poster design using the template attached as a reference. I have also included our Dravolun logo to put on the poster. Please DO NOT use the graphics in the flyer as we are expecting something much better :-)

-Size needed 11x17 with bleeding for printing

-We need this made in Photoshop (CS3 friendly) or at least delivered in PS as we might change some text or re-arrange the design later on.

-We need this in layers.

```html
<!DOCTYPE html>
<html lang="en">
<head>
<meta charset="utf-8">
<title>Dravolun Bootcamps – Fresh Start, Bold Body Makeover Contest</title>
<link href="https://fonts.googleapis.com/css2?family=Stardos+Stencil:wght@700&family=Roboto:wght@400;500;700&display=swap" rel="stylesheet">
<style>
  :root {
    --paper: #eef0f1;
    --frame-blue: #3f6e9e;
    --panel-top: #8fb0cf;
    --panel-bottom: #c7d6e3;
    --brand-blue: #1f5fa8;
    --accent-orange: #b96a22;
    --ink: #1e1f22;
    --headline-light: #f2f3f2;
    --rule: #b97a3c;
  }
  * { margin: 0; padding: 0; box-sizing: border-box; }
  html, body { width: 900px; height: 1200px; overflow: hidden; background: #d9d9d9; }
  .poster {
    position: relative; width: 900px; height: 1200px;
    background: var(--paper);
    font-family: "Roboto", Arial, sans-serif; color: var(--ink);
  }
  .poster-frame {
    position: absolute; left: 30px; top: 30px; right: 30px; bottom: 30px;
    background: linear-gradient(180deg, #4f7eae 0%, var(--frame-blue) 100%);
  }
  .poster-panel {
    position: absolute; left: 54px; top: 54px; right: 54px; bottom: 54px;
    background: linear-gradient(180deg, var(--panel-top) 0%, #aec5da 40%, var(--panel-bottom) 100%);
  }
  .block { position: absolute; left: 0; width: 900px; text-align: center; }
  .brand {
    top: 96px; font-family: "Roboto", Arial, sans-serif; font-weight: 700;
    font-size: 54px; letter-spacing: 2px; color: var(--ink); line-height: 1.1;
  }
  .brand-mark {
    display: inline-block; width: 28px; height: 28px; background: var(--ink);
    margin-right: 14px; vertical-align: middle; position: relative; top: -4px;
  }
  .headline { font-family: "Stardos Stencil", "Georgia", serif; font-weight: 700; line-height: 1; }
  .headline-intro { top: 240px; font-size: 50px; color: var(--headline-light); letter-spacing: 1px; }
  .headline-main { top: 296px; font-size: 54px; color: var(--brand-blue); letter-spacing: 1px; }
  .headline-contest { top: 356px; font-size: 112px; color: var(--accent-orange); }
  .rule {
    position: absolute; left: 123px; width: 654px; height: 5px;
    border-top: 2px solid var(--rule); border-bottom: 1px solid var(--rule);
  }
  .rule-1 { top: 471px; } .rule-2 { top: 568px; } .rule-3 { top: 926px; } .rule-4 { top: 1078px; }
  .promise { top: 488px; font-size: 29px; font-weight: 500; line-height: 40px; text-transform: uppercase; }
  .stars { position: absolute; left: 395px; width: 110px; height: 24px; }
  .stars-top { top: 593px; } .stars-bottom { top: 878px; }
  .laurel {
    position: absolute; top: 634px; width: 120px; height: 240px;
    background: var(--brand-blue); opacity: .9; border-radius: 60px;
  }
  .laurel-left { left: 105px; } .laurel-right { left: 675px; }
  .schedule-label {
    font-family: "Stardos Stencil", "Georgia", serif; font-weight: 700;
    font-size: 23px; color: var(--brand-blue); letter-spacing: 1px;
  }
  .schedule-value { font-size: 25px; color: var(--ink); margin-top: 4px; }
  .schedule-kickoff { top: 632px; } .schedule-start { top: 717px; } .schedule-end { top: 801px; }
  .offer { top: 942px; font-size: 28px; font-weight: 500; line-height: 38px; text-transform: uppercase; }
  .prize { top: 1034px; font-size: 28px; font-weight: 500; text-transform: uppercase; }
  .price { color: var(--accent-orange); font-weight: 700; }
  .website {
    top: 1098px; font-family: "Stardos Stencil", "Georgia", serif; font-weight: 700;
    font-size: 27px; color: var(--brand-blue); letter-spacing: .5px;
  }
  .website-note { top: 1128px; font-size: 18px; color: var(--brand-blue); }
</style>
</head>
<body>
<main class="poster">
  <div class="poster-frame"></div>
  <div class="poster-panel" role="img" aria-label="Faded blue camouflage texture background"></div>

  <div class="block brand"><span class="brand-mark"></span>DRAVOLUN BOOTCAMPS</div>

  <h1>
    <span class="block headline headline-intro">FRESH START, BOLD BODY</span>
    <span class="block headline headline-main">MAKEOVER</span>
    <span class="block headline headline-contest">CONTEST</span>
  </h1>

  <div class="rule rule-1"></div>
  <p class="block promise">In just 6 weeks, transform your body<br>and get in the best shape of your life!</p>
  <div class="rule rule-2"></div>

  <svg class="stars stars-top" viewBox="0 0 110 24" aria-hidden="true">
    <g fill="#2a2a2a">
      <polygon points="15,4 18,11 25,11 19.5,15.5 21.5,22 15,18 8.5,22 10.5,15.5 5,11 12,11"/>
      <polygon points="55,0 59,9 68,9 61,15 64,24 55,19 46,24 49,15 42,9 51,9"/>
      <polygon points="95,4 98,11 105,11 99.5,15.5 101.5,22 95,18 88.5,22 90.5,15.5 85,11 92,11"/>
    </g>
  </svg>

  <div class="laurel laurel-left" role="img" aria-label="Blue laurel branch ornament"></div>
  <div class="laurel laurel-right" role="img" aria-label="Blue laurel branch ornament"></div>

  <div class="block schedule-kickoff">
    <div class="schedule-label">KICK OFF MEETING:</div>
    <div class="schedule-value">Thursday, Jan 14 at 7:30 pm</div>
  </div>
  <div class="block schedule-start">
    <div class="schedule-label">START DATE:</div>
    <div class="schedule-value">Monday, January 18th</div>
  </div>
  <div class="block schedule-end">
    <div class="schedule-label">END DATE:</div>
    <div class="schedule-value">Friday, February 26th</div>
  </div>

  <svg class="stars stars-bottom" viewBox="0 0 110 24" aria-hidden="true">
    <g fill="#2a2a2a">
      <polygon points="15,4 18,11 25,11 19.5,15.5 21.5,22 15,18 8.5,22 10.5,15.5 5,11 12,11"/>
      <polygon points="55,0 59,9 68,9 61,15 64,24 55,19 46,24 49,15 42,9 51,9"/>
      <polygon points="95,4 98,11 105,11 99.5,15.5 101.5,22 95,18 88.5,22 90.5,15.5 85,11 92,11"/>
    </g>
  </svg>

  <div class="rule rule-3"></div>
  <p class="block offer">6 weeks of training, nutrition, and<br>coaching starting at just <span class="price">$99</span>!</p>
  <p class="block prize"><span class="price">$500</span> cash prize for winner!</p>
  <div class="rule rule-4"></div>

  <p class="block website">WWW.DRAVOLUNBOOTCAMPS.COM</p>
  <p class="block website-note">visit for more info</p>
</main>
</body>
</html>
```